electrical contractor business card for professional modern company

I need a business card design for an electrical contractors business. I do all kinds of electricical work from new homes, air conditioning, data and communications. I have a logo design i want on it and have a good idea in my head of what i want it to look like. I like simple yet bold and professional looking. All black background is a must

Target Market(s)

Anyone needing electrical work done

Industry/Entity Type

Electrical

Contact Information for Business Card

company name- KTW Electrical and Data
person name-martin pellowe
phone number- 0418 362 927
website-ktwelec.example.com.au

Font styles to use
Sans Serif

Requirements
Must have
• email
• website
• logo
• name
• phone number
• list of work i do:
• -electrical
• -air-conditioning
• -data/communications
• -cctv/security
• -domestic/commercial/industrial
• -24hr emergency breakdown repair
Nice to have
• i would like the logo on the front side in the centre taking up most of the card with black background.
• on the rear i want the list of work i do with company info i.e. email, website, my name, phone number. rear of card also black background with orange writing to match the orange in the logo

```html
<!DOCTYPE html>
<html lang="en">
<head>
<meta charset="utf-8">
<title>KTW Electrical and Data — Business Card</title>
<link rel="stylesheet" href="https://fonts.googleapis.com/css2?family=Ubuntu:wght@300;400;500&display=swap">
<style>
  :root {
    --stage: #9a9a9a;
    --card: #0c0d0f;
    --card-edge: #1b1d21;
    --orange: #f26a1b;
    --orange-soft: #e0895a;
    --faint: #2a2c30;
    --divider: #5a3a28;
  }
  * { box-sizing: border-box; margin: 0; padding: 0; }
  html, body {
    width: 1200px;
    height: 800px;
    overflow: hidden;
    background: var(--stage);
    font-family: "Ubuntu", sans-serif;
  }
  .stage {
    position: relative;
    width: 1200px;
    height: 800px;
    display: flex;
    align-items: center;
    justify-content: center;
    gap: 48px;
  }
  .card {
    position: relative;
    width: 504px;
    height: 288px;
    background: linear-gradient(160deg, var(--card-edge) 0%, var(--card) 55%);
    border-radius: 4px;
    box-shadow: 0 14px 30px rgba(0,0,0,0.35);
    color: var(--orange);
    overflow: hidden;
  }

  /* Rear: contact side */
  .card-rear .holder-name {
    position: absolute;
    top: 30px;
    right: 34px;
    font-size: 40px;
    font-weight: 400;
    letter-spacing: 0.5px;
    text-transform: capitalize;
  }
  .card-rear .holder-role {
    position: absolute;
    top: 82px;
    right: 36px;
    font-size: 15px;
    font-weight: 300;
    color: var(--orange-soft);
  }
  .card-rear .services {
    position: absolute;
    top: 60px;
    left: 34px;
    font-size: 12px;
    line-height: 15px;
    font-weight: 300;
  }
  .card-rear .services-intro { margin-bottom: 1px; }
  .card-rear .services-list { list-style: none; }
  .card-rear .services-list li {
    position: relative;
    padding-left: 14px;
  }
  .card-rear .services-list li::before {
    content: "";
    position: absolute;
    left: 0;
    top: 4px;
    width: 8px;
    height: 8px;
    border-radius: 50%;
    background: var(--orange);
  }
  .card-rear .contact-line {
    position: absolute;
    left: 34px;
    bottom: 30px;
    display: flex;
    align-items: center;
    gap: 10px;
    font-size: 15px;
    font-weight: 300;
  }
  .card-rear .phone-icon { width: 14px; height: 14px; }
  .card-rear .contact-divider {
    width: 1px;
    height: 22px;
    background: var(--divider);
  }
  .card-rear .brand-faint {
    position: absolute;
    right: 34px;
    bottom: 76px;
    font-size: 26px;
    font-weight: 500;
    color: var(--faint);
  }

  /* Front: brand side */
  .card-front {
    display: flex;
    align-items: center;
    justify-content: center;
  }
  .card-front .brand-name {
    font-size: 30px;
    font-weight: 500;
    letter-spacing: 1px;
    text-transform: uppercase;
    color: var(--orange);
  }
</style>
</head>
<body>
  <main class="stage">
    <section class="card card-rear" aria-label="Business card, contact side">
      <h1 class="holder-name">martin pellowe</h1>
      <p class="holder-role">Electrical contractors</p>
      <div class="services">
        <p class="services-intro">I do all kinds of electrical work</p>
        <ul class="services-list">
          <li>electrical</li>
          <li>air-conditioning</li>
          <li>data/communications</li>
          <li>cctv/security</li>
          <li>domestic/commercial/industrial</li>
          <li>24hr emergency breakdown repair</li>
        </ul>
      </div>
      <p class="brand-faint">KTW Electrical and Data</p>
      <div class="contact-line">
        <svg class="phone-icon" viewBox="0 0 14 14" aria-hidden="true">
          <circle cx="7" cy="7" r="7" fill="var(--orange)"/>
          <path d="M4.6 3.6l1.3-.2.7 1.8-.9.7c.4.9 1.1 1.6 2 2l.7-.9 1.8.7-.2 1.3c-3 .2-5.6-2.4-5.4-5.4z" fill="var(--card)"/>
        </svg>
        <span class="phone">0418 362 927</span>
        <span class="contact-divider"></span>
        <span class="website">website-ktwelec.example.com.au</span>
      </div>
    </section>

    <section class="card card-front" aria-label="Business card, brand side">
      <p class="brand-name">KTW Electrical and Data</p>
    </section>
  </main>
</body>
</html>
```